Velmora - 3D medical animations and high end visual content

Our company creates high end visual content and animations for medical global companies.
Our website - www.velmora-studio.example
We would like to have an amazing business card for our CEO that he can use in the following exhebitions he is going to attend.
It is very important that the design will be memorable and diffrent. It has to reflect our brand design (you can have it from our website)
We would like to transmit innovation, prestige, luxury, aesthetics.
The card has to be Double Sided

Target Market(s)

Marketing managers in medical global companys

Industry/Entity Type

It Company

Contact Information for Business Card

Requirements
Nice to have
• It is very important that the design will be memorable and diffrent. It has to reflect our brand design (you can have it from our website)

```html
<!DOCTYPE html>
<html lang="en">
<head>
<meta charset="utf-8">
<title>Velmora – Business Card</title>
<link rel="stylesheet" href="https://fonts.googleapis.com/css2?family=Montserrat:wght@500;700&family=Arimo:wght@400&display=swap">
<style>
  :root {
    --page-bg: #2a2a2a;
    --card-bg: #070707;
    --ink: #ffffff;
    --ink-soft: #e6e6e6;
    --accent-gold: #f2c21b;
    --accent-cyan: #1ba6c4;
  }
  * { box-sizing: border-box; margin: 0; padding: 0; }
  html, body {
    width: 1200px; height: 900px; overflow: hidden;
    background: var(--page-bg);
  }
  .sheet {
    width: 1200px; height: 900px;
    display: flex; flex-direction: column;
    align-items: center; justify-content: center; gap: 40px;
  }
  .card {
    width: 700px; height: 400px;
    background: var(--card-bg);
    position: relative;
    box-shadow: 0 12px 30px rgba(0,0,0,.45);
  }
  .wordmark {
    font-family: "Montserrat", sans-serif;
    font-weight: 500;
    color: var(--ink);
    letter-spacing: 3px;
    line-height: 1;
  }
  .card--front {
    display: flex; align-items: center; justify-content: center;
  }
  .card--front .wordmark { font-size: 58px; }

  .card--back .wordmark {
    position: absolute; left: 70px; top: 176px;
    font-size: 46px;
  }
  .divider {
    position: absolute; left: 392px; top: 92px;
    width: 2px; height: 188px;
    background: var(--accent-gold);
  }
  .contact {
    position: absolute; left: 418px; top: 92px;
    font-family: "Arimo", sans-serif;
    color: var(--ink-soft);
  }
  .contact__name {
    font-family: "Montserrat", sans-serif;
    font-weight: 700;
    font-size: 22px; letter-spacing: 2px;
    color: var(--accent-gold);
  }
  .contact__role { font-size: 15px; margin-top: 4px; margin-bottom: 16px; }
  .contact__list { list-style: none; }
  .contact__item {
    display: flex; align-items: center; gap: 10px;
    font-size: 15px; height: 26px;
  }
  .contact__icon { width: 16px; height: 16px; flex: none; }
  .contact__icon * { fill: none; stroke: var(--accent-cyan); stroke-width: 1.6; stroke-linecap: round; stroke-linejoin: round; }
</style>
</head>
<body>
<main class="sheet">
  <section class="card card--front" aria-label="Card front">
    <span class="wordmark">VELMORA</span>
  </section>

  <section class="card card--back" aria-label="Card back">
    <span class="wordmark">VELMORA</span>
    <div class="divider"></div>
    <div class="contact">
      <p class="contact__name">NOAM HALEVI</p>
      <p class="contact__role">Founder &amp; CEO</p>
      <ul class="contact__list">
        <li class="contact__item">
          <svg class="contact__icon" viewBox="0 0 16 16"><rect x="4" y="1.5" width="8" height="13" rx="1.5"/><line x1="7" y1="12" x2="9" y2="12"/></svg>
          +972-50-1234567
        </li>
        <li class="contact__item">
          <svg class="contact__icon" viewBox="0 0 16 16"><path d="M3 2l3 0 1 3-2 1.5a8 8 0 0 0 4.5 4.5L11 9l3 1 0 3a1.5 1.5 0 0 1-1.5 1.5A11 11 0 0 1 1.5 3.5 1.5 1.5 0 0 1 3 2z"/></svg>
          +972-70-7654321
        </li>
        <li class="contact__item">
          <svg class="contact__icon" viewBox="0 0 16 16"><rect x="1.5" y="3.5" width="13" height="9" rx="1"/><path d="M1.5 4l6.5 5 6.5-5"/></svg>
          noam@velmora-studio.example
        </li>
        <li class="contact__item">
          <svg class="contact__icon" viewBox="0 0 16 16"><circle cx="8" cy="8" r="6.5"/><ellipse cx="8" cy="8" rx="3" ry="6.5"/><line x1="1.5" y1="8" x2="14.5" y2="8"/></svg>
          www.velmora-studio.example
        </li>
      </ul>
    </div>
  </section>
</main>
</body>
</html>
```